Tumble Nest - mobile play centre poster designs

Who are we - we are a mobile playground business that specialises in providing entertainment to children in a safe, clean environment either at home or in a function centre. Brief - create 4 different signs to be displayed on our playgrounds. Please find attached 3 photos from our competitors to use as a guide. Corflute sign - size A1 Toddler zone - size A1 Playground rules - size A4 No climbing - size 20cmx8cm sending through photos and documents now.
Colors
Designer to choose colors to be used in the design.
Requirements
Must have
- Colour, be very specific with the rules, pictures

```html
<!DOCTYPE html>
<html lang="en">
<head>
<meta charset="utf-8">
<title>Tumble Nest – Play Ground Rules</title>
<link rel="stylesheet" href="https://fonts.googleapis.com/css2?family=Anton&family=Roboto:wght@700;900&family=Roboto+Condensed:wght@700&display=swap">
<style>
  :root {
    --red: #e3202a;
    --green: #3aa935;
    --ink: #1a1a1a;
    --paper: #ffffff;
    --art-warm: #e9d6c4;
    --art-cool: #d7dde4;
  }
  * { box-sizing: border-box; margin: 0; padding: 0; }
  html, body { width: 849px; height: 1200px; overflow: hidden; background: var(--paper); }
  .poster { position: relative; width: 849px; height: 1200px; background: var(--paper); }
  .poster__frame {
    position: absolute; inset: 22px; border: 12px solid var(--red); border-radius: 30px;
  }
  .brand {
    position: absolute; left: 78px; top: 44px; width: 270px;
    display: flex; flex-direction: column; align-items: flex-start;
  }
  .brand__name {
    font-family: 'Anton', sans-serif; font-size: 52px; line-height: 1; color: var(--red);
    text-transform: uppercase; letter-spacing: 1px;
  }
  .brand__tag {
    font-family: 'Roboto', sans-serif; font-weight: 900; font-size: 15px; color: var(--ink);
    letter-spacing: 1px; margin-top: 6px;
  }
  .section-title {
    position: absolute; left: 372px; top: 66px;
    font-family: 'Roboto', sans-serif; font-weight: 900; font-size: 44px; color: var(--green);
    letter-spacing: 0.5px;
  }
  .notice {
    position: absolute; left: 60px; right: 60px; top: 150px; text-align: center;
    font-family: 'Roboto', sans-serif; font-weight: 900; font-size: 31px; line-height: 1.2; color: var(--ink);
  }
  .headline {
    position: absolute; left: 0; right: 0; top: 238px; text-align: center;
    font-family: 'Anton', sans-serif; font-size: 104px; line-height: 1.1; color: var(--green);
  }
  .rules { position: absolute; left: 110px; top: 366px; width: 690px; list-style: none; }
  .rule { display: flex; align-items: center; height: 103px; }
  .rule__no {
    width: 180px; font-family: 'Anton', sans-serif; font-size: 96px; line-height: 1; color: var(--red);
  }
  .rule__text {
    flex: 1; font-family: 'Roboto Condensed', sans-serif; font-weight: 700; font-size: 25px;
    line-height: 1.1; color: var(--ink); text-transform: uppercase;
  }
  .rule__icon { width: 170px; height: 92px; display: flex; justify-content: flex-end; align-items: center; }
  .rule__icon svg { display: block; }
</style>
</head>
<body>
<main class="poster">
  <div class="poster__frame"></div>

  <header>
    <div class="brand">
      <span class="brand__name">Tumble Nest</span>
      <span class="brand__tag">MOBILE PLAY CENTRE</span>
    </div>
    <h2 class="section-title">PLAYGROUNDS</h2>
  </header>

  <p class="notice">Parents/Guardians must supervise children<br>using this play equipment at all times</p>

  <h1 class="headline">Play Ground Rules</h1>

  <ul class="rules">
    <li class="rule">
      <span class="rule__no">NO</span>
      <span class="rule__text">Shoes – socks<br>must be worn</span>
      <span class="rule__icon">
        <svg width="170" height="92" viewBox="0 0 170 92">
          <rect x="0" y="8" width="82" height="76" rx="8" fill="var(--art-cool)" role="img" aria-label="Illustration of a pair of sneakers"/>
          <path d="M104 46 h22 M115 35 v22" stroke="var(--red)" stroke-width="7" stroke-linecap="round"/>
          <rect x="132" y="8" width="38" height="76" rx="8" fill="var(--art-cool)" role="img" aria-label="Illustration of a pair of socks"/>
        </svg>
      </span>
    </li>
    <li class="rule">
      <span class="rule__no">NO</span>
      <span class="rule__text">Climbing the nets</span>
      <span class="rule__icon">
        <svg width="92" height="92" viewBox="0 0 92 92">
          <rect x="3" y="3" width="86" height="86" rx="8" fill="var(--paper)" stroke="var(--ink)" stroke-width="4"/>
          <rect x="14" y="14" width="64" height="64" fill="var(--art-cool)" role="img" aria-label="Illustration of a child climbing a net"/>
          <circle cx="46" cy="46" r="36" fill="none" stroke="var(--red)" stroke-width="7"/>
          <line x1="21" y1="21" x2="71" y2="71" stroke="var(--red)" stroke-width="7"/>
        </svg>
      </span>
    </li>
    <li class="rule">
      <span class="rule__no">NO</span>
      <span class="rule__text">Food or drink</span>
      <span class="rule__icon">
        <svg width="92" height="92" viewBox="0 0 92 92">
          <rect x="3" y="3" width="86" height="86" rx="8" fill="var(--paper)" stroke="var(--ink)" stroke-width="4"/>
          <rect x="14" y="14" width="64" height="64" fill="var(--art-warm)" role="img" aria-label="Illustration of a burger and a drink cup"/>
          <circle cx="46" cy="46" r="36" fill="none" stroke="var(--red)" stroke-width="7"/>
          <line x1="21" y1="21" x2="71" y2="71" stroke="var(--red)" stroke-width="7"/>
        </svg>
      </span>
    </li>
    <li class="rule">
      <span class="rule__no">NO</span>
      <span class="rule__text">Bottle or glass</span>
      <span class="rule__icon">
        <svg width="92" height="92" viewBox="0 0 92 92">
          <rect x="3" y="3" width="86" height="86" rx="8" fill="var(--paper)" stroke="var(--ink)" stroke-width="4"/>
          <rect x="14" y="14" width="64" height="64" fill="var(--art-warm)" role="img" aria-label="Illustration of a bottle and a glass"/>
          <circle cx="46" cy="46" r="36" fill="none" stroke="var(--red)" stroke-width="7"/>
          <line x1="21" y1="21" x2="71" y2="71" stroke="var(--red)" stroke-width="7"/>
        </svg>
      </span>
    </li>
    <li class="rule">
      <span class="rule__no">NO</span>
      <span class="rule__text">Chewing gum</span>
      <span class="rule__icon">
        <svg width="92" height="92" viewBox="0 0 92 92">
          <rect x="3" y="3" width="86" height="86" rx="8" fill="var(--paper)" stroke="var(--ink)" stroke-width="4"/>
          <rect x="14" y="14" width="64" height="64" fill="var(--art-cool)" role="img" aria-label="Illustration of sticks of chewing gum"/>
          <circle cx="46" cy="46" r="36" fill="none" stroke="var(--red)" stroke-width="7"/>
          <line x1="21" y1="21" x2="71" y2="71" stroke="var(--red)" stroke-width="7"/>
        </svg>
      </span>
    </li>
    <li class="rule">
      <span class="rule__no">NO</span>
      <span class="rule__text">Sharp objects</span>
      <span class="rule__icon">
        <svg width="92" height="92" viewBox="0 0 92 92">
          <rect x="3" y="3" width="86" height="86" rx="8" fill="var(--paper)" stroke="var(--ink)" stroke-width="4"/>
          <rect x="14" y="14" width="64" height="64" fill="var(--art-cool)" role="img" aria-label="Illustration of scissors and a knife"/>
          <circle cx="46" cy="46" r="36" fill="none" stroke="var(--red)" stroke-width="7"/>
          <line x1="21" y1="21" x2="71" y2="71" stroke="var(--red)" stroke-width="7"/>
        </svg>
      </span>
    </li>
    <li class="rule">
      <span class="rule__no">NO</span>
      <span class="rule__text">Face painting</span>
      <span class="rule__icon">
        <svg width="92" height="92" viewBox="0 0 92 92">
          <rect x="3" y="3" width="86" height="86" rx="8" fill="var(--paper)" stroke="var(--ink)" stroke-width="4"/>
          <rect x="14" y="14" width="64" height="64" fill="var(--art-warm)" role="img" aria-label="Illustration of face paint and brushes"/>
          <circle cx="46" cy="46" r="36" fill="none" stroke="var(--red)" stroke-width="7"/>
          <line x1="21" y1="21" x2="71" y2="71" stroke="var(--red)" stroke-width="7"/>
        </svg>
      </span>
    </li>
  </ul>
</main>
</body>
</html>
```